Construction material supplies company business card ****

1. Full company name “K R Mortar Works Ltd”
I am after a Business card design for the company as a whole. We are better known in Solomon Islands as “K R Mortar” for short.

We are a building materials supplier of
Ready Mixed Concrete, Bricks and Blocks,
Quarry products- gravel, aggregates, sand etc.
Cement distributor/retailer of reputable brands.
Other prefab concrete products. Culverts, wave breakers, concrete retaining blocks etc.

2. Competitive Advantage over Competition: Quality, efficient, professional, dependable, reliable

3. We want people to feel trust worthy, high quality, strong when they see our brand

5. No preference to color. Maybe more sturdy and corporate. Not fancy.

Industry/Entity Type

CONSTRUCTION SUPPLY

Contact Information for Business Card

Name, Position, office phone mob phone, email

Requirements
Must have
• the company logo
Nice to have
• would like to see a mixture of designs, of with logo only and also with simple graphic designs to bring out the company whilst still have the strong sturdy professional feeling

```html
<!DOCTYPE html>
<html lang="en">
<head>
<meta charset="utf-8">
<title>K R Mortar – Business Card</title>
<link href="https://fonts.googleapis.com/css2?family=Josefin+Sans:wght@400;600;700&display=swap" rel="stylesheet">
<style>
  :root {
    --navy: #1d4373;
    --navy-deep: #1a3a66;
    --indigo: #2e2f8f;
    --indigo-dark: #16155e;
    --sky: #5f93d2;
    --white: #ffffff;
    --stage: #e9e6e1;
    --ink: #1f4470;
  }
  * { margin: 0; padding: 0; box-sizing: border-box; }
  html, body {
    width: 1200px; height: 994px; overflow: hidden;
    background: var(--stage);
    font-family: "Josefin Sans", sans-serif;
  }
  .sheet { position: relative; width: 1200px; height: 994px; }
  .card {
    position: absolute; left: 250px; width: 700px; height: 400px;
    overflow: hidden; box-shadow: 0 6px 18px rgba(0,0,0,.18);
  }

  /* Logo side */
  .card--brand {
    top: 72px;
    background: radial-gradient(ellipse at 55% 40%, var(--indigo) 0%, #2b3a86 45%, var(--navy) 100%);
    color: var(--white);
    text-align: center;
  }
  .brand-mark {
    display: flex; align-items: center; justify-content: center; gap: 18px;
    margin-top: 112px;
  }
  .brand-mark__square { width: 34px; height: 34px; background: var(--white); }
  .brand-mark__name {
    font-weight: 700; font-size: 52px; letter-spacing: 4px; line-height: 1;
    text-transform: uppercase; padding-top: 6px;
  }
  .services { margin-top: 54px; font-size: 17px; letter-spacing: 1px; line-height: 1.6; }

  /* Contact side */
  .card--contact { top: 522px; background: var(--navy); }
  .contact__top {
    position: absolute; inset: 0 0 auto 0; height: 215px; background: var(--white);
  }
  .contact__stripe {
    position: absolute; left: 0; right: 0; top: 215px; height: 6px;
    background: linear-gradient(90deg, var(--indigo) 0%, var(--sky) 45%, var(--indigo) 75%, var(--indigo-dark) 100%);
  }
  .contact__bottom {
    position: absolute; left: 0; right: 0; top: 221px; bottom: 0;
    background: linear-gradient(120deg, var(--navy-deep) 0%, var(--navy) 60%, #21497c 100%);
  }
  .contact__logo {
    position: absolute; top: 82px; left: 250px;
    display: flex; align-items: center; gap: 16px; color: var(--ink);
  }
  .contact__logo .brand-mark__square { background: var(--ink); width: 30px; height: 30px; }
  .contact__logo .brand-mark__name { font-size: 46px; }
  .person {
    position: absolute; right: 370px; top: 262px; text-align: right; color: var(--white);
  }
  .person__name { font-size: 38px; line-height: 1; }
  .person__name b { font-weight: 700; }
  .person__role { font-size: 15px; letter-spacing: 1.5px; margin-top: 6px; }
  .divider {
    position: absolute; left: 358px; top: 238px; width: 1px; height: 144px;
    background: rgba(255,255,255,.35);
  }
  .details {
    position: absolute; left: 378px; top: 236px; list-style: none; color: var(--white);
    font-size: 15px; line-height: 27px;
  }
  .details li { display: flex; align-items: center; gap: 10px; }
  .details svg { width: 14px; height: 14px; flex: none; fill: var(--white); }
  .details .indent { padding-left: 24px; }
</style>
</head>
<body>
<main class="sheet">

  <section class="card card--brand" aria-label="Business card, logo side">
    <div class="brand-mark">
      <span class="brand-mark__square"></span>
      <span class="brand-mark__name">K R Mortar</span>
    </div>
    <p class="services">
      Ready Mixed Concrete – Bricks &amp; Blocks – Gravel – Aggregates – Sand<br>
      – Cement Distributor/Retailer – Culverts – Wave Breakers –<br>
      – Concrete Retaining Blocks &amp; many more –
    </p>
  </section>

  <section class="card card--contact" aria-label="Business card, contact side">
    <div class="contact__top"></div>
    <div class="contact__stripe"></div>
    <div class="contact__bottom"></div>

    <div class="contact__logo">
      <span class="brand-mark__square"></span>
      <span class="brand-mark__name">K R Mortar</span>
    </div>

    <div class="person">
      <p class="person__name">Daniel <b>Reyes</b></p>
      <p class="person__role">Sales Executive</p>
    </div>

    <div class="divider"></div>

    <ul class="details">
      <li>
        <svg viewBox="0 0 16 16"><path d="M2 6c0-2 3-3.5 6-3.5S14 4 14 6v1.5h-3V6H5v1.5H2zM4 8h8l1.5 5.5h-11z"/></svg>
        555-201-4830
      </li>
      <li>
        <svg viewBox="0 0 16 16"><path d="M4.5 1h7a1 1 0 0 1 1 1v12a1 1 0 0 1-1 1h-7a1 1 0 0 1-1-1V2a1 1 0 0 1 1-1zm1 2v9h5V3zm2.5 10a.8.8 0 1 0 0 .01z"/></svg>
        555-318-7264
      </li>
      <li>
        <svg viewBox="0 0 16 16"><path d="M1 4h14v9H1zm1.5 1.2v.4L8 9.2l5.5-3.6v-.4z"/></svg>
        dan.reyes@krmortar.com
      </li>
      <li>
        <svg viewBox="0 0 16 16"><path d="M8 1a7 7 0 1 0 0 14A7 7 0 0 0 8 1zm0 1.5c.8 0 1.7 1.7 2 4.5H6c.3-2.8 1.2-4.5 2-4.5zM2.6 7h2.1c0-1.5.3-2.9.7-3.8A5.5 5.5 0 0 0 2.6 7zm8.7 0h2.1a5.5 5.5 0 0 0-2.8-3.8c.4.9.7 2.3.7 3.8zM2.6 9a5.5 5.5 0 0 0 2.8 3.8c-.4-.9-.7-2.3-.7-3.8zM6 9c.3 2.8 1.2 4.5 2 4.5s1.7-1.7 2-4.5zm5.3 0c0 1.5-.3 2.9-.7 3.8A5.5 5.5 0 0 0 13.4 9z"/></svg>
        www.krmortar.com
      </li>
      <li>
        <svg viewBox="0 0 16 16"><path d="M8 1a5 5 0 0 0-5 5c0 3.6 5 9 5 9s5-5.4 5-9a5 5 0 0 0-5-5zm0 7a2 2 0 1 1 0-4 2 2 0 0 1 0 4z"/></svg>
        18 Harbour Road, Unit 4
      </li>
      <li class="indent">Point Cruz, Honiara 00677</li>
    </ul>
  </section>

</main>
</body>
</html>
```